Modern Spot UV Business Card design

We are a relatively new real estate agency. We need a business card that reflects the professionalism and prestige of our company but is also modern and fresh, based around our logo.
We would love to utilise spot UV.
Happy to let the designers use their imagination and see what they come up with (we're not very creative, so have no ideas for you, sorry) :-)
We'd like one for each staff member, but I've just provided one staff members photo here to avoid confusion.

Target Market(s)

Families

Industry/Entity Type

Real Estate Agent

Contact Information for Business Card

Colin Varga - Director & Principal
Mobile: 0491 527 806
Email: colin.varga@vbrokers.example.com.au
Phone: (08) 7364 9150
Fax: (08) 7364 9182
www.vargabrokersrealestate.example.com.au

Font styles to use
Other font styles liked:
• Kabel Dm BT

Requirements
Must have
• Contact details, logo, photo, spot UV
Nice to have
• Modern interesting features that will make people comment. Nothing too feminine nor too masculine.
Should not have
• No houses! Nothing typical of a real estate agent.

```html
<!DOCTYPE html>
<html lang="en">
<head>
<meta charset="utf-8">
<title>VargaBrokers Real Estate – Business Card</title>
<link href="https://fonts.googleapis.com/css2?family=Open+Sans:wght@400;600;700&display=swap" rel="stylesheet">
<style>
  :root{
    --stage:#3b3b3b;
    --card-black:#161616;
    --card-deep:#101010;
    --uv:#2c2c2c;
    --uv-soft:#242424;
    --photo-light:#b4b4b4;
    --photo-mid:#8f8f8f;
    --photo-dark:#5d6166;
    --panel:#1b1b1b;
    --white:#ffffff;
    --accent:#2aa6e0;
  }
  *{margin:0;padding:0;box-sizing:border-box}
  html,body{width:802px;height:1200px;overflow:hidden}
  body{background:var(--stage);font-family:"Open Sans",Arial,sans-serif;position:relative}

  .card{position:absolute;left:51px;width:700px;height:400px;overflow:hidden;box-shadow:0 18px 40px rgba(0,0,0,.45)}
  .card--front{top:150px;background:var(--card-black)}
  .card--back{top:650px;background:var(--panel)}

  /* front */
  .front__wave{position:absolute;inset:0}
  .front__brand{position:absolute;left:0;right:0;top:160px;display:flex;justify-content:center;align-items:center;gap:18px}
  .front__brand-mark{width:26px;height:26px;background:var(--uv)}
  .front__name{font-weight:700;font-size:66px;letter-spacing:-1px;color:var(--uv);line-height:1}

  /* back */
  .back__photo{position:absolute;left:0;top:0;width:430px;height:400px;
    background:radial-gradient(ellipse at 45% 45%,var(--photo-light) 0%,var(--photo-mid) 55%,var(--photo-dark) 100%)}
  .back__panel{position:absolute;left:410px;top:0;width:290px;height:400px;background:var(--panel);
    box-shadow:-18px 0 28px rgba(0,0,0,.35)}
  .back__brand{position:absolute;left:24px;top:22px;display:flex;align-items:center;gap:8px;
    font-weight:600;font-size:14px;color:var(--white)}
  .back__brand-dot{width:10px;height:10px;border-radius:50%;background:var(--accent)}
  .back__person{position:absolute;right:300px;bottom:36px;text-align:right;color:var(--white)}
  .back__person-name{font-weight:700;font-size:28px;letter-spacing:.5px;text-transform:uppercase;line-height:1.05}
  .back__person-role{font-weight:400;font-size:17px;line-height:1.3}

  .contact{position:absolute;left:20px;top:70px;width:254px;color:var(--white)}
  .contact__phones{display:flex;gap:12px;align-items:flex-start}
  .contact__icons{display:flex;flex-direction:column;gap:8px;padding-top:3px}
  .contact__icons svg{width:14px;height:14px}
  .contact__numbers{font-size:16px;line-height:22px;font-weight:600}
  .contact__rule{height:2px;background:linear-gradient(90deg,transparent,var(--accent),transparent);margin:20px 0}
  .contact__web-icons{display:flex;gap:10px;margin-bottom:10px}
  .contact__web-icons svg{width:14px;height:14px}
  .contact__line{font-size:11.5px;line-height:20px;font-weight:400;white-space:nowrap}
</style>
</head>
<body>

<section class="card card--front" aria-label="Card front">
  <svg class="front__wave" viewBox="0 0 700 400" aria-hidden="true">
    <path d="M0 400 L0 250 C120 200 260 140 400 170 C520 195 600 110 700 60 L700 400 Z" fill="var(--card-deep)"/>
    <path d="M330 400 C420 300 520 250 700 240 L700 400 Z" fill="var(--uv-soft)" opacity=".5"/>
  </svg>
  <div class="front__brand">
    <span class="front__brand-mark"></span>
    <span class="front__name">VargaBrokers</span>
  </div>
</section>

<section class="card card--back" aria-label="Card back">
  <div class="back__photo" role="img" aria-label="Portrait photo of Colin Varga in a grey suit"></div>
  <div class="back__brand"><span class="back__brand-dot"></span>VargaBrokers</div>
  <div class="back__person">
    <div class="back__person-name">Colin Varga</div>
    <div class="back__person-role">Director &amp; Principal</div>
  </div>

  <div class="back__panel">
    <div class="contact">
      <div class="contact__phones">
        <div class="contact__icons">
          <svg viewBox="0 0 14 14" aria-hidden="true"><rect x="3.5" y="1" width="7" height="12" rx="1.5" fill="none" stroke="var(--accent)" stroke-width="1.5"/></svg>
          <svg viewBox="0 0 14 14" aria-hidden="true"><path d="M2 5 C2 2 12 2 12 5 L10 6 L9 4.5 L5 4.5 L4 6 Z M4 7 L10 7 L12 12 L2 12 Z" fill="var(--accent)"/></svg>
          <svg viewBox="0 0 14 14" aria-hidden="true"><rect x="4" y="1" width="6" height="4" fill="var(--accent)"/><rect x="1.5" y="5.5" width="11" height="7" rx="1" fill="var(--accent)"/></svg>
        </div>
        <div class="contact__numbers">
          0491 527 806<br>(08) 7364 9150<br>(08) 7364 9182
        </div>
      </div>
      <div class="contact__rule"></div>
      <div class="contact__web-icons">
        <svg viewBox="0 0 14 14" aria-hidden="true"><rect x="1" y="3" width="12" height="8" fill="none" stroke="var(--accent)" stroke-width="1.4"/><path d="M1 3 L7 8 L13 3" fill="none" stroke="var(--accent)" stroke-width="1.4"/></svg>
        <svg viewBox="0 0 14 14" aria-hidden="true"><circle cx="7" cy="7" r="5.8" fill="none" stroke="var(--accent)" stroke-width="1.3"/><ellipse cx="7" cy="7" rx="2.5" ry="5.8" fill="none" stroke="var(--accent)" stroke-width="1.1"/><path d="M1.2 7 H12.8" stroke="var(--accent)" stroke-width="1.1"/></svg>
      </div>
      <div class="contact__line">colin.varga@vbrokers.example.com.au</div>
      <div class="contact__line">www.vargabrokersrealestate.example.com.au</div>
      <div class="contact__rule"></div>
    </div>
  </div>
</section>

</body>
</html>
```